Book cover for LS

Design cover for a book of gratitude and inspiration.
Book trim size will be 6.5 x 6.5 inches, or 8 x 8 inches, hardcover, 96 pages
Title: Lantern Stones
Subtitle: A Book of Gratitude and Inspiration
Author: Carl Wendover

```html
<!DOCTYPE html>
<html lang="en">
<head>
<meta charset="utf-8">
<title>Lantern Stones — Book Cover</title>
<link rel="stylesheet" href="https://fonts.googleapis.com/css2?family=Marcellus&family=Cormorant+Garamond:wght@600&family=Allison&display=swap">
<style>
  :root {
    --backdrop: #a47d69;
    --cream: #f8f0d2;
    --parchment: #ece6c6;
    --sage: #cfd8bf;
    --ink: #6b4541;
    --flower-amber: #d9a85a;
    --flower-rose: #b98a86;
    --meadow-dark: #3b2d3d;
  }
  * { margin: 0; padding: 0; box-sizing: border-box; }
  html, body {
    width: 1200px;
    height: 1200px;
    overflow: hidden;
    background: var(--backdrop);
  }
  .cover {
    position: absolute;
    left: 160px;
    top: 160px;
    width: 880px;
    height: 880px;
    overflow: hidden;
    background: radial-gradient(ellipse at 85% 0%, var(--cream) 0%, transparent 55%),
                linear-gradient(180deg, var(--parchment) 0%, var(--sage) 70%);
  }
  .rule {
    position: absolute;
    height: 2px;
    background: var(--ink);
  }
  .rule--top { left: 72px; right: 72px; top: 58px; }
  .title {
    position: absolute;
    left: 72px;
    top: 72px;
    width: 736px;
    height: 240px;
  }
  .title text {
    font-family: "Marcellus", serif;
    fill: var(--ink);
  }
  .subtitle {
    position: absolute;
    left: 72px;
    right: 72px;
    top: 318px;
    text-align: center;
    font-family: "Allison", cursive;
    font-size: 68px;
    line-height: 1;
    color: var(--ink);
    white-space: nowrap;
  }
  .author-row {
    position: absolute;
    left: 72px;
    right: 72px;
    top: 398px;
    display: flex;
    align-items: center;
    gap: 24px;
  }
  .author-row .line {
    flex: 1;
    height: 2px;
    background: var(--ink);
  }
  .author {
    font-family: "Cormorant Garamond", serif;
    font-weight: 600;
    font-size: 30px;
    letter-spacing: 0.5px;
    color: var(--ink);
    white-space: nowrap;
  }
  .meadow {
    position: absolute;
    left: 0;
    right: 0;
    top: 480px;
    bottom: 0;
    background: linear-gradient(180deg,
      rgba(207,216,191,0) 0%,
      rgba(217,168,90,0.55) 22%,
      var(--flower-rose) 45%,
      #6e5258 65%,
      var(--meadow-dark) 100%);
  }
</style>
</head>
<body>
  <main class="cover">
    <div class="rule rule--top"></div>
    <svg class="title" viewBox="0 0 736 240" aria-label="Lantern Stones">
      <text x="0" y="100" font-size="108" textLength="736" lengthAdjust="spacingAndGlyphs">LANTERN</text>
      <text x="0" y="230" font-size="150" textLength="736" lengthAdjust="spacingAndGlyphs">STONES</text>
    </svg>
    <p class="subtitle">A Book of Gratitude and Inspiration</p>
    <div class="author-row">
      <span class="line"></span>
      <span class="author">CARL WENDOVER</span>
      <span class="line"></span>
    </div>
    <div class="meadow" role="img" aria-label="Vintage-toned photograph of a field of white, pink and golden cosmos flowers against a pale sky"></div>
  </main>
</body>
</html>
```